Business Card Design for Concierge business

Hi. I would like to have an elegant, smart business card for my concierge business, called Harbor Concierge. The services I provide are mail management, dog walking, cleaning, car, stylist, personal shopper, running errands, property management, event planning. I was thinking to add my picture but I would like to see options without it as well, if possible.

Thank you.

Business Card Details:
*Designers are to solely use contact information for the business card design. This is not to be used to contact the customer*

Name: Tamsin Heller
mail: quaylineerrands@mailvora.net
Phone: 305-482-9167

Target Market(s)

vacation home owners

Industry/Entity Type

Business

Font styles to use
Serif

Colors

Designer to choose colors to be used in the design.

Requirements
Nice to have
• Could use icons that describe the services I provide for example car, house, key, shopping cart, shopping bags, envelope, champagne glasses, phone, dog etc.

```html
<!DOCTYPE html>
<html lang="en">
<head>
<meta charset="utf-8">
<title>Harbor Concierge – Business Cards</title>
<link href="https://fonts.googleapis.com/css2?family=Playfair+Display:wght@400;600&display=swap" rel="stylesheet">
<style>
  :root{
    --blue:#3a56a8;
    --blue-deep:#2f4794;
    --gold:#c9a13b;
    --white:#ffffff;
    --stage:#161616;
  }
  *{box-sizing:border-box;margin:0;padding:0}
  html,body{width:1200px;height:900px;overflow:hidden;background:var(--stage)}
  body{position:relative;font-family:"Playfair Display",Georgia,serif}

  .card{position:absolute;left:250px;width:700px;height:400px;background:var(--white);overflow:hidden;box-shadow:0 10px 30px rgba(0,0,0,.5)}
  .card--front{top:30px}
  .card--back{top:470px}

  .wordmark{position:absolute;color:var(--blue);font-weight:600;line-height:1}
  .wordmark__main{display:block;font-size:72px}
  .wordmark__sub{display:block;font-size:38px;margin-top:2px;padding-left:80px}
  .card--front .wordmark{left:110px;top:60px}
  .card--back .wordmark{left:255px;top:14px}
  .card--back .wordmark__main{font-size:56px}
  .card--back .wordmark__sub{font-size:30px;padding-left:64px}

  .portrait{position:absolute;left:470px;top:110px;width:200px;height:235px;
    background:linear-gradient(160deg,#d9cfc6 0%,#8a7a6c 45%,#2b2522 100%);border-radius:90px 90px 0 0}

  .contact-band{position:absolute;left:0;bottom:0;width:100%;height:55px;background:var(--blue);
    display:flex;align-items:center;gap:16px;padding-left:40px;color:var(--white);font-size:15px;white-space:nowrap}
  .contact-band__name{font-weight:600}
  .contact-band__divider{width:1px;height:18px;background:rgba(255,255,255,.5)}
  .contact-band__item{display:flex;align-items:center;gap:8px}
  .contact-band__icon{width:18px;height:18px;border-radius:50%;background:var(--gold);display:flex;align-items:center;justify-content:center}

  .services{position:absolute;left:0;top:120px;width:100%;height:280px;
    background:linear-gradient(180deg,var(--blue) 0%,var(--blue-deep) 100%)}
  .service{position:absolute;width:124px;margin-left:-62px;text-align:center;color:var(--white);font-size:13px;line-height:1.3}
  .service__icon{width:58px;height:58px;margin:0 auto 6px;border-radius:50%;background:var(--white);
    display:flex;align-items:center;justify-content:center}
  .service__icon svg{width:34px;height:34px}
</style>
</head>
<body>

<section class="card card--front">
  <div class="wordmark">
    <span class="wordmark__main">Harbor</span>
    <span class="wordmark__sub">Concierge</span>
  </div>
  <div class="portrait" role="img" aria-label="Portrait photo of Tamsin Heller"></div>
  <div class="contact-band">
    <span class="contact-band__name">Tamsin Heller</span>
    <span class="contact-band__divider"></span>
    <span class="contact-band__item">
      <span class="contact-band__icon"><svg width="10" height="8" viewBox="0 0 10 8"><rect x=".5" y=".5" width="9" height="7" fill="none" stroke="#fff"/><path d="M.5 .5 5 4.5 9.5 .5" fill="none" stroke="#fff"/></svg></span>
      quaylineerrands@mailvora.net
    </span>
    <span class="contact-band__divider"></span>
    <span class="contact-band__item">
      <span class="contact-band__icon"><svg width="10" height="10" viewBox="0 0 10 10"><path d="M2 1 4 3 3 4.5Q4.5 6.5 5.5 7L7 6l2 2-1.5 1.5Q4 9 .5 2.5Z" fill="#fff"/></svg></span>
      305-482-9167
    </span>
  </div>
</section>

<section class="card card--back">
  <div class="wordmark">
    <span class="wordmark__main">Harbor</span>
    <span class="wordmark__sub">Concierge</span>
  </div>
  <div class="services">
    <div class="service" style="left:95px;top:22px">
      <div class="service__icon"><svg viewBox="0 0 34 34"><path d="M5 20 8 12h18l3 8v6H5Z" fill="var(--blue)"/><circle cx="10" cy="26" r="3" fill="#fff"/><circle cx="24" cy="26" r="3" fill="#fff"/><rect x="10" y="14" width="14" height="5" fill="#fff"/></svg></div>Car</div>
    <div class="service" style="left:222px;top:22px">
      <div class="service__icon"><svg viewBox="0 0 34 34"><ellipse cx="17" cy="22" rx="6" ry="5" fill="var(--blue)"/><circle cx="9" cy="14" r="2.6" fill="var(--blue)"/><circle cx="14" cy="9" r="2.6" fill="var(--blue)"/><circle cx="20" cy="9" r="2.6" fill="var(--blue)"/><circle cx="25" cy="14" r="2.6" fill="var(--blue)"/></svg></div>Dog walking</div>
    <div class="service" style="left:350px;top:22px">
      <div class="service__icon"><svg viewBox="0 0 34 34"><path d="M8 13h16l-2 15H10Z" fill="var(--blue)"/><path d="M9 13Q16 4 23 13" fill="none" stroke="var(--blue)" stroke-width="2"/><circle cx="26" cy="8" r="2" fill="none" stroke="var(--blue)"/></svg></div>Cleaning</div>
    <div class="service" style="left:478px;top:22px">
      <div class="service__icon"><svg viewBox="0 0 34 34"><rect x="5" y="9" width="24" height="17" rx="2" fill="var(--blue)"/><path d="M6 10 17 19 28 10M6 25l8-7M28 25l-8-7" fill="none" stroke="#fff" stroke-width="1.5"/></svg></div>Mail management</div>
    <div class="service" style="left:605px;top:22px">
      <div class="service__icon"><svg viewBox="0 0 34 34"><path d="M17 11V9a2.5 2.5 0 1 1 2.5-2.5" fill="none" stroke="var(--blue)" stroke-width="2"/><path d="M17 11 4 22h26Z" fill="none" stroke="var(--blue)" stroke-width="2.5" stroke-linejoin="round"/><rect x="8" y="24" width="18" height="4" fill="var(--blue)"/></svg></div>Stylist</div>

    <div class="service" style="left:158px;top:146px">
      <div class="service__icon"><svg viewBox="0 0 34 34"><path d="M4 8h5l3 13h14l3-10H11" fill="none" stroke="var(--blue)" stroke-width="2.5"/><rect x="12" y="12" width="15" height="8" fill="var(--blue)"/><circle cx="14" cy="26" r="2.2" fill="var(--blue)"/><circle cx="24" cy="26" r="2.2" fill="var(--blue)"/></svg></div>Personal shopper</div>
    <div class="service" style="left:286px;top:146px">
      <div class="service__icon"><svg viewBox="0 0 34 34"><rect x="6" y="6" width="16" height="22" rx="2" fill="var(--blue)"/><path d="M9 12l2 2 3-3M9 19l2 2 3-3" fill="none" stroke="#fff" stroke-width="1.6"/><path d="M22 17h8M26 13l4 4-4 4" fill="none" stroke="var(--blue)" stroke-width="2.4"/></svg></div>Running errands</div>
    <div class="service" style="left:414px;top:146px">
      <div class="service__icon"><svg viewBox="0 0 34 34"><path d="M3 17 17 5l14 12" fill="none" stroke="var(--blue)" stroke-width="3"/><path d="M8 16v13h7v-7h4v7h7V16L17 8Z" fill="var(--blue)"/></svg></div>Property management</div>
    <div class="service" style="left:542px;top:146px">
      <div class="service__icon"><svg viewBox="0 0 34 34"><path d="M7 6h8l-1 9a3 3 0 0 1-6 0Z" fill="var(--blue)"/><path d="M11 18v9M7 28h8" stroke="var(--blue)" stroke-width="2"/><path d="M19 6h8l-1 9a3 3 0 0 1-6 0Z" fill="var(--blue)"/><path d="M23 18v9M19 28h8" stroke="var(--blue)" stroke-width="2"/></svg></div>Event planning</div>
  </div>
</section>

</body>
</html>
```